Bramwell Joinery Website

My client Bramwell Joinery is looking for a redesign for a Word Press Website. Their current site is at www.bramwelljoinery.example They are a custom cabinet company, but also create bathroom, living room, bar and entertainment and bedroom cabinets too. They would like a design that emulates the master craftsman work they do yet a contemporary style.

Their current site was designed using Flash elements.

Target Market(s)

Home owners and builders of high end homes

Industry/Entity Type

Entertainment

Font styles to use
Serif
Decorative

Requirements
Must have
• Must show their work and logo using a contemporary style.
Nice to have
• Sliders that showcase their projects.

```html
<!DOCTYPE html>
<html lang="en">
<head>
<meta charset="utf-8">
<title>Bramwell Joinery</title>
<link href="https://fonts.googleapis.com/css2?family=Open+Sans:wght@400;600;700&family=Arimo:wght@400;700&display=swap" rel="stylesheet">
<style>
:root{
  --green:#3aab3a;
  --green-bright:#4cbb4a;
  --green-dark:#1f7a26;
  --nav:#3b3b3b;
  --ink:#1e1e1e;
  --card:#f6f6f6;
  --footer:#0f0f0f;
  --white:#fff;
}
*{margin:0;padding:0;box-sizing:border-box}
html,body{width:702px;height:1200px;overflow:hidden;background:var(--white)}
body{position:relative;font-family:"Arimo",Arial,sans-serif;color:var(--ink)}
.abs{position:absolute}

.topbar{left:0;top:0;width:702px;height:26px;background:var(--green);border-bottom:2px solid var(--green-dark)}
.social{right:92px;top:6px;display:flex;gap:6px}
.social span{width:14px;height:14px;border-radius:50%;background:var(--white);display:block}
.brand-tab{left:274px;top:-40px;width:134px;height:136px;border-radius:0 0 67px 67px;background:var(--white);border:2px solid #d9d9d9;border-top:none}
.brand{left:274px;top:40px;width:134px;text-align:center;font-family:"Open Sans",sans-serif;font-weight:700;font-size:14px;line-height:17px;color:var(--green)}
.brand-dot{left:333px;top:16px;width:16px;height:16px;border-radius:50%;background:var(--green)}
.call{right:60px;top:82px;font-family:"Open Sans",sans-serif;font-size:12px;color:#555;display:flex;align-items:center;gap:4px}
.call b{font-weight:400;font-size:15px;color:var(--green)}

.nav{left:0;top:109px;width:702px;height:27px;background:var(--nav)}
.nav ul{list-style:none;display:flex;height:27px;padding-left:58px}
.nav li{color:var(--white);font-size:8.5px;line-height:27px;padding:0 10.5px;text-transform:uppercase}
.nav li.active{background:var(--green);padding:0 15px}

.hero{left:0;top:136px;width:702px;height:252px;
  background:
    linear-gradient(180deg,rgba(255,255,255,0) 70%,rgba(190,160,120,.35) 100%),
    linear-gradient(90deg,#f7f5ef 0%,#eef0e6 12%,#f3ece0 30%,#eadfcb 48%,#e6d6bb 60%,#ead9bc 78%,#d9c09b 90%,#b8986e 100%)}
.hero-title{left:62px;top:252px;width:256px;height:64px;background:rgba(255,255,255,.55);padding:4px 0 0 8px;font-family:"Open Sans",sans-serif;font-weight:700;font-size:26px;line-height:28px}
.hero-title .g{color:var(--green)}
.hero-title .d{color:#3c3c3c}

.why{left:0;top:403px;width:702px;text-align:center;font-family:"Open Sans",sans-serif;font-weight:700;font-size:18px;color:var(--green)}
.intro{left:60px;top:446px;width:584px;text-align:center;font-size:7.6px;line-height:12.8px;color:#222}
.intro p+p{margin-top:12.8px}

.card{top:584px;width:184px;height:170px;background:var(--card);border:1px solid #e2e2e2}
.card h3{margin-top:11px;text-align:center;font-family:"Open Sans",sans-serif;font-weight:600;font-size:12.5px;color:#222;text-transform:uppercase}
.card .frame{margin:5px auto 0;width:161px;height:75px;background:#dcdcdc;padding:5px}
.card .photo{width:100%;height:100%}
.card p{margin:6px 10px 0;text-align:center;font-size:7px;line-height:10.5px;color:#333}
.more{left:53px;bottom:0;width:64px;height:22px;border-radius:32px 32px 0 0;background:var(--green);color:var(--white);font-family:"Open Sans",sans-serif;font-weight:700;font-size:8.5px;text-align:center;line-height:24px;letter-spacing:.5px}

.projects{left:0;top:795px;width:702px;height:237px;background:var(--green-bright)}
.projects h2{position:absolute;top:18px;width:702px;text-align:center;font-size:17px;font-weight:700;color:var(--white)}
.projects .sub{position:absolute;top:42px;width:702px;text-align:center;font-family:"Open Sans",sans-serif;font-size:10.5px;color:var(--white)}
.shot{top:75px;width:177px;height:124px;border:1px solid rgba(255,255,255,.8)}
.shot-kitchen{left:74px;background:linear-gradient(135deg,#e8e2d6,#d4cbbb 50%,#2e3440 90%)}
.shot-island{left:266px;background:linear-gradient(135deg,#d9d2c6,#2a2422 45%,#6b3e22)}
.shot-oven{left:459px;background:linear-gradient(135deg,#5a5a5a,#bdbdbd 40%,#efebe4 70%,#7a4a2a)}
.arrow{top:118px;width:19px;height:26px;background:#111;border-radius:2px}

.footer{left:0;top:1032px;width:702px;height:168px;background:var(--footer)}
.footer h4{position:absolute;top:13px;font-family:"Open Sans",sans-serif;font-weight:400;font-size:14px;color:var(--green)}
.links{left:65px;top:40px;list-style:none;font-family:"Open Sans",sans-serif;font-size:9px;line-height:16.5px;color:var(--white)}
.field{height:16px;background:var(--white);font-size:7.5px;color:#888;padding-left:4px;line-height:16px}
.submit{left:378px;top:90px;width:62px;height:20px;background:var(--green);color:var(--white);font-family:"Open Sans",sans-serif;font-weight:600;font-size:10px;text-align:center;line-height:20px;border-radius:2px}
.contact{left:478px;top:42px;width:180px;font-family:"Open Sans",sans-serif;font-size:8px;line-height:14px;color:var(--white);font-weight:600}
.rule{left:60px;top:1156px;width:578px;height:1px;background:#333}
.copy{left:68px;top:1172px;font-size:8px;color:#ddd}
</style>
</head>
<body>

<div class="abs topbar"></div>
<div class="abs social" aria-label="Social links"><span></span><span></span><span></span><span></span><span></span></div>
<div class="abs brand-tab"></div>
<div class="abs brand-dot"></div>
<div class="abs brand">Bramwell<br>Joinery</div>
<div class="abs call">Call Now:
  <svg width="11" height="11" viewBox="0 0 24 24"><path fill="#444" d="M6.6 10.8a15.1 15.1 0 0 0 6.6 6.6l2.2-2.2c.3-.3.7-.4 1-.2 1.1.4 2.3.6 3.6.6.6 0 1 .4 1 1V20c0 .6-.4 1-1 1A17 17 0 0 1 3 4c0-.6.4-1 1-1h3.5c.6 0 1 .4 1 1 0 1.3.2 2.5.6 3.6.1.3 0 .7-.2 1z"/></svg>
  <b>+123-555-0142</b></div>

<nav class="abs nav"><ul>
  <li class="active">Home</li><li>Who we are</li><li>Getting started</li><li>Customer experience</li><li>Professional</li><li>Portfolio</li><li>Cabinet hardware</li>
</ul></nav>

<div class="abs hero" role="img" aria-label="Bright living room with a wall-mounted TV cabinet, lounge chair and round coffee table"></div>
<div class="abs hero-title"><div class="g">20 YEARS</div><div class="d">OF INNOVATIONS</div></div>

<h1 class="abs why">Why work Bramwell Joinery ?</h1>
<div class="abs intro">
  <p>Working from the largestdatabase of industry professionalsin Australia, Crestline Staffing operates exclusively in the Mining, Oil &amp; Gas, Construction and Engineering sectors. Our clients range from engineering consultancies and major owner-operator oil companies to international EPCM's and the largest diversified mining companies in the world. In addition to providing Health, Safety, Environment and Quality professionals, we also deliver highly qualified and experienced Risk Management, Emergency Response and Training personnel at all levels.</p>
  <p>Today's dynamic and ever-changing workplaces require recruiters to up the ante – that's where we come in. With offices in Perth, Brisbane,Seoul and Hong Kong, we source both locally and internationally to meet the unique requirements of our clients and candidates. Our passion for the industry and commitment to ensuring a safer work environment for all is the foundation of everything we do.</p>
</div>

<div class="abs card" style="left:60px">
  <h3>Cabinets for dining</h3>
  <div class="frame"><div class="photo" role="img" aria-label="White dining kitchen with island" style="background:linear-gradient(90deg,#6b5440,#d8d2c8 45%,#eeeae4)"></div></div>
  <p>Vestibulum rutrum pharetra diam, eget dapibus leo vehicula ut. Fusce aliquam, odio eget pharetra diam, eget dapibus leo vehicula ut.</p>
  <div class="abs more">MORE</div>
</div>
<div class="abs card" style="left:258px">
  <h3>Cabinets dor kitchens</h3>
  <div class="frame"><div class="photo" role="img" aria-label="Dark wood kitchen island cabinet" style="background:linear-gradient(90deg,#cfcac2,#1c1a1a 30%,#2a2422 75%,#6a4a36)"></div></div>
  <p>Vestibulum rutrum pharetra diam, eget dapibus leo vehicula ut. Fusce aliquam, odio eget pharetra diam, eget dapibus leo vehicula ut.</p>
  <div class="abs more">MORE</div>
</div>
<div class="abs card" style="left:458px">
  <h3>Cabinets for bathrooms</h3>
  <div class="frame"><div class="photo" role="img" aria-label="White cabinetry with built-in steel oven" style="background:linear-gradient(90deg,#4a4a4a,#9a9a9a 35%,#efece6 60%,#ddd6cc)"></div></div>
  <p>Vestibulum rutrum pharetra diam, eget dapibus leo vehicula ut. Fusce aliquam, odio eget pharetra diam, eget dapibus leo vehicula ut.</p>
  <div class="abs more">MORE</div>
</div>

<section class="abs projects">
  <h2>RECENT PROJECTS</h2>
  <div class="sub">Since the inception of the firm in the year 1999 Bramwell has developed into one of the innovative</div>
  <div class="abs arrow" style="left:10px"><svg width="19" height="26" viewBox="0 0 19 26"><path d="M12 6 6 13l6 7" stroke="#fff" stroke-width="1.6" fill="none"/></svg></div>
  <div class="abs shot shot-kitchen" role="img" aria-label="White kitchen with range hood, pendant lights and marble island"></div>
  <div class="abs shot shot-island" role="img" aria-label="Black kitchen island on dark wood floor"></div>
  <div class="abs shot shot-oven" role="img" aria-label="White cabinetry with stainless oven on wood floor"></div>
  <div class="abs arrow" style="left:667px"><svg width="19" height="26" viewBox="0 0 19 26"><path d="M7 6l6 7-6 7" stroke="#fff" stroke-width="1.6" fill="none"/></svg></div>
</section>

<footer class="abs footer">
  <h4 style="left:65px">Navigation Links</h4>
  <h4 style="left:265px">Free Report</h4>
  <h4 style="left:478px">Contact Us</h4>
  <ul class="abs links"><li>Home</li><li>About Us</li><li>Why Holloway Group</li><li>Services</li></ul>
  <div class="abs field" style="left:266px;top:42px;width:80px">Name</div>
  <div class="abs field" style="left:361px;top:42px;width:79px">Company</div>
  <div class="abs field" style="left:266px;top:67px;width:174px">Email Address</div>
  <div class="abs submit">Submit</div>
  <div class="abs contact">
    Bramwell Joinery &amp; Fixtures<br>
    <i>Office tel:</i> +123(555)0198<br>
    <i>Mobile:</i> +920000142, <i>K.Rowe:</i> +4550173<br>
    Harbour Lane, Westgate opposite to the marina, Kestrel Bay.
  </div>
</footer>
<div class="abs rule"></div>
<div class="abs copy">Copyright © 2014 Bramwell Joinery. All right reseverd.</div>

</body>
</html>
```